WP website design (Brenn)

We need a wordpress design for an established auction and real estate company based in Tennessee. The winning design will incorporate a professional color scheme with company logo in a clean layout. The design needs to consider that this will be developed on a responsive theme. Colors are those that will highlight the logo.

Industry/Entity Type

Real Estate

Font styles to use
Sans Serif

Colors

Designer to choose colors to be used in the design.

Requirements
Must have
• Navigation: 1) Home - with auctions as content as seen at http://vornelbidhouse.com/ 2) Current Auctions 3) Past Auctions 4) Referrals 5) Why Auction 6) About Us 7) Contact Us

Header will have logo, contact info, Social icons (Facebook, Twitter, Youtube) and tagline "Bid Smart With Brenn!' Slideshow (use stock real estate image for image) will be used either in header or content area.

Widgets: Email signup form, Upcoming Auctions, Register for Online Bidding text, testimonials

Footer will have contact info (below) smaller company logo, and the association logos attached.

```html
<!DOCTYPE html>
<html lang="en">
<head>
<meta charset="utf-8">
<title>Brenn Auctions inc.</title>
<link href="https://fonts.googleapis.com/css2?family=Arimo:wght@400;700&family=Oswald:wght@500&display=swap" rel="stylesheet">
<style>
:root{
  --header:#1d1d1d;
  --body:#2b2b2b;
  --dark:#232323;
  --gold:#f8b840;
  --gold-text:#e8a526;
  --teal:#0e8a8c;
  --teal-dark:#0b7274;
  --ink:#222;
  --white:#fff;
}
*{margin:0;padding:0;box-sizing:border-box}
html,body{width:847px;height:1200px;overflow:hidden}
body{position:relative;background:var(--body);font-family:"Arimo",Arial,sans-serif;color:var(--white)}
.abs{position:absolute}
.site-header{left:0;top:0;width:847px;height:96px;background:var(--header)}
.logo{left:82px;top:36px;font-size:22px;font-weight:700;color:#2bb3b0;letter-spacing:.5px}
.search{left:466px;top:41px;width:173px;height:26px;background:var(--white);border:1px solid #ccc;color:#777;font-size:12px;padding:6px 7px}
.search svg{position:absolute;right:7px;top:5px}
.social{top:38px;width:28px;height:28px;border-radius:50%}
.main-nav{left:0;top:96px;width:847px;height:36px;background:var(--gold)}
.main-nav a{position:absolute;top:14px;font-size:9.5px;font-weight:700;color:#5a4320;text-decoration:none;letter-spacing:.3px}
.main-nav a.current{left:82px;top:6px;width:57px;height:24px;background:var(--dark);color:var(--white);border-radius:4px;text-align:center;line-height:24px}
.hero{left:0;top:132px;width:847px;height:349px;background:var(--teal);border-bottom:1px solid #6ccfcf}
.hero svg{position:absolute;left:0;top:0}
.caption{left:280px;top:202px;width:290px;height:37px;background:rgba(40,40,40,.75);font-size:20px;text-align:center;line-height:37px}
.dot{top:315px;width:10px;height:10px;border-radius:50%;background:#eee}
.section-head{top:481px;height:38px;background:linear-gradient(#2e2e2e,#1a1a1a);border:1px solid #111;border-top:none;border-radius:0 0 4px 4px;font-family:"Oswald",sans-serif;font-size:15px;line-height:38px;padding-left:35px;text-transform:uppercase}
.section-head::before{content:"";position:absolute;left:13px;top:13px;width:12px;height:12px;border-radius:50%;background:#eee}
.section-head::after{content:"";position:absolute;left:17px;top:16px;border-left:5px solid #222;border-top:3px solid transparent;border-bottom:3px solid transparent}
.event-photo{left:89px;width:109px;height:128px;border:3px solid #999;background:linear-gradient(#b6c9d6 0%,#7d7a6e 45%,#555 60%,#3c3c3c 100%)}
.event{left:208px;width:300px;font-size:9px;line-height:14px;color:#e6e6e6}
.event h3{font-size:9.5px;color:var(--gold-text);margin-bottom:1px}
.event b{color:var(--white)}
.event p.desc{margin-top:8px;width:298px;font-size:9.3px;letter-spacing:.1px}
.btn{display:inline-block;height:19px;line-height:19px;border-radius:3px;font-size:9px;font-weight:700;padding:0 7px;margin-top:8px;margin-right:8px;vertical-align:top}
.btn i{display:inline-block;width:9px;height:7px;background:var(--white);margin-right:5px;vertical-align:-1px;border-radius:1px}
.btn-teal{background:var(--teal)}
.btn-dark{background:#1c1c1c}
.rule{left:89px;width:406px;height:1px;background:#4a4a4a}
.signup{left:547px;top:539px;width:193px;height:138px;background:var(--white);border-radius:4px;color:var(--ink);padding:10px 10px}
.signup h4,.testi h4{font-size:15px;font-weight:700}
.signup h4 span,.testi h4 span{color:var(--teal)}
.field{width:166px;height:22px;border:1px solid #ccc;border-radius:3px;background:linear-gradient(#ddd,#f5f5f5);font-size:8.5px;font-style:italic;color:#999;padding:6px 6px}
.subscribe{left:114px;top:103px;width:62px;height:22px;background:#333;border:2px solid #999;border-radius:4px;color:var(--white);font-size:9.5px;font-weight:700;text-align:center;line-height:18px}
.register{left:548px;top:694px;width:193px;height:100px;background:linear-gradient(var(--teal),var(--teal-dark));border:1px solid #6cd2d0;border-radius:4px;padding:13px 14px}
.register h4{font-size:15px;font-weight:700;line-height:18px}
.register h4 span{color:var(--gold)}
.reg-field{left:14px;top:58px;width:166px;height:22px;border:1px solid #0a5f60;border-radius:3px;background:var(--teal-dark);font-size:8.5px;font-style:italic;padding:6px 6px}
.reg-field span{position:absolute;right:0;top:0;height:20px;width:52px;background:#e3e3e3;color:#333;font-style:normal;font-size:10px;text-align:center;line-height:20px}
.testi{left:550px;top:811px;width:192px;height:202px;background:linear-gradient(#dcdcdc,#b9b9b9);border-radius:3px;color:var(--ink);padding:10px 10px}
.testi-photo{left:10px;top:39px;width:161px;height:76px;border:2px solid #a93d2a;border-radius:3px;background:linear-gradient(90deg,#6a4a33,#a1693f,#4f3324,#8b5a36)}
.testi p{left:12px;top:122px;width:165px;font-size:8.5px;line-height:13px;color:#444}
.more{left:120px;top:182px;width:62px;height:12px;background:var(--white);border-radius:6px;font-size:7.5px;font-style:italic;color:#555;text-align:center;line-height:12px}
.partners{left:70px;top:1042px;width:707px;height:76px;background:var(--white)}
.badge{top:22px;height:36px;background:#3a3a3a;border-radius:3px}
.site-footer{left:0;top:1093px;width:847px;height:107px;background:#1f1f1f;z-index:-1}
.footer-links{left:70px;top:1142px;font-size:9px;line-height:17px;color:#ddd}
.footer-logo{left:676px;top:1145px;font-size:15px;font-weight:700;color:#b5b5b5}
</style>
</head>
<body>
<header class="site-header abs">
  <div class="logo abs">Brenn Auctions inc.</div>
  <div class="search abs">Search
    <svg width="15" height="15" viewBox="0 0 15 15"><circle cx="6" cy="6" r="4.5" fill="none" stroke="#111" stroke-width="2"/><line x1="9.5" y1="9.5" x2="13.5" y2="13.5" stroke="#111" stroke-width="2.4"/></svg>
  </div>
  <span class="social abs" style="left:653px;background:#1d5c99"></span>
  <span class="social abs" style="left:685px;background:#27a7e0"></span>
  <span class="social abs" style="left:717px;background:#f39a1d"></span>
  <span class="social abs" style="left:749px;background:#b5b5b5"></span>
</header>

<nav class="main-nav abs">
  <a class="current" href="#">HOME</a>
  <a href="#" style="left:176px">CURRENT AUCTIONS</a>
  <a href="#" style="left:322px">PAST AUCTIONS</a>
  <a href="#" style="left:429px">REFERRALS</a>
  <a href="#" style="left:518px">WHY AUCTIONS</a>
  <a href="#" style="left:625px">ABOUT US</a>
</nav>

<section class="hero abs">
  <svg width="847" height="349" viewBox="0 132 847 349">
    <defs>
      <linearGradient id="houseTones" x1="0" y1="0" x2="0" y2="1">
        <stop offset="0" stop-color="#b9cfe4"/>
        <stop offset=".35" stop-color="#8a6e5c"/>
        <stop offset=".65" stop-color="#6d625a"/>
        <stop offset=".85" stop-color="#5f8f3a"/>
        <stop offset="1" stop-color="#3f6f2a"/>
      </linearGradient>
    </defs>
    <path d="M84 148H763V362Q423.5 508 84 362Z" fill="#fff"/>
    <path d="M90 154H757V358Q423.5 496 90 358Z" fill="url(#houseTones)" role="img" aria-label="Photo of a large suburban family home with gabled roofs and a front lawn"/>
  </svg>
  <div class="caption abs">“BID SMART WITH BRENN!”..</div>
  <span class="dot abs" style="left:406px"></span>
  <span class="dot abs" style="left:420px;background:var(--gold)"></span>
  <span class="dot abs" style="left:434px"></span>
  <span class="dot abs" style="left:449px"></span>
</section>

<h2 class="section-head abs" style="left:89px;width:325px">Upcoming Events</h2>
<h2 class="section-head abs" style="left:546px;width:207px">Recent Photos</h2>

<div class="event-photo abs" style="top:537px" role="img" aria-label="Photo of a street corner with a brick house"></div>
<article class="event abs" style="top:543px">
  <h3>ABSOLUTE AUCTION</h3>
  <b>Begins:</b> Saturday, March 16, 2013 at 10:00 AM EDT<br>
  <b>Location:</b> 2158 Millbrook Road Dalton, KY 40119
  <p class="desc">Kestrel BS3F High Lift, simply dummy text of the printing and type-setting industry simply dummy text of the printing and typesetting industry 600 Series Harlan tractor w/Tolland Loader, Dune buggy,</p>
  <span class="btn btn-teal"><i></i>Details</span><span class="btn btn-dark"><i></i>Details</span>
</article>
<div class="rule abs" style="top:680px"></div>

<div class="event-photo abs" style="top:695px" role="img" aria-label="Photo of a street corner with a brick house"></div>
<article class="event abs" style="top:699px">
  <h3>ABSOLUTE AUCTION</h3>
  <b>Begins:</b> Saturday, March 16, 2013 at 10:00 AM<br>
  <b>Location:</b> 2158 Millbrook Road Dalton, KY
  <p class="desc">Kestrel BS3F High Lift, simply dummy text of the printing and type-setting industry simply dummy text of the printing and typesetting industry 600 Series Harlan tractor w/Tolland Loader, Dune buggy,</p>
  <span class="btn btn-teal"><i></i>Details</span><span class="btn btn-dark"><i></i>Details</span>
</article>
<div class="rule abs" style="top:838px"></div>

<div class="event-photo abs" style="top:863px" role="img" aria-label="Photo of a street corner with a brick house"></div>
<article class="event abs" style="top:868px">
  <h3>ABSOLUTE AUCTION</h3>
  <b>Begins:</b> Saturday, March 16, 2013 at 10:00 AM<br>
  <b>Location:</b> 2158 Millbrook Road Dalton, KY
  <p class="desc">Kestrel BS3F High Lift, simply dummy text of the printing and type-setting industry simply dummy text of the printing and typesetting industry 600 Series Harlan tractor w/Tolland Loader, Dune buggy,</p>
  <span class="btn btn-teal"><i></i>Details</span><span class="btn btn-dark"><i></i>Details</span>
</article>

<aside class="signup abs">
  <h4>Email <span>Signup</span> Form</h4>
  <div class="field" style="margin-top:9px">Email Address</div>
  <div class="field" style="margin-top:11px">Password</div>
  <div class="subscribe abs">Subscribe</div>
</aside>

<aside class="register abs">
  <h4>Register for<br><span>Online Bidding Text</span></h4>
  <div class="reg-field abs">Email Address<span>Register</span></div>
</aside>

<aside class="testi abs">
  <h4>Client &nbsp;<span>Testimonials</span></h4>
  <div class="testi-photo abs" role="img" aria-label="Photo of antiques and furniture set out for auction"></div>
  <p class="abs">Vestibulum rutrum pharetra diam, eget dapibus leo vehicula ut. Fusce aliquam, odio eget adipiscing lobortis, nisl sapien placerat est...</p>
  <div class="more abs">More Details »</div>
</aside>

<div class="site-footer abs"></div>
<section class="partners abs" aria-label="Associations">
  <span class="badge abs" style="left:50px;width:40px"></span>
  <span class="badge abs" style="left:120px;width:84px"></span>
  <span class="badge abs" style="left:238px;width:48px"></span>
  <span class="badge abs" style="left:316px;width:78px"></span>
  <span class="badge abs" style="left:423px;width:80px"></span>
  <span class="badge abs" style="left:549px;width:36px"></span>
  <span class="badge abs" style="left:630px;width:36px"></span>
</section>

<footer>
  <div class="footer-links abs">Home - Upcoming Auctions - Past Auctions - Referrals- About Us - Contact Us<br>Copyright © 2014 Brenn Auctions inc. All Rights Reserved</div>
  <div class="footer-logo abs">Brenn Auctions inc.</div>
</footer>
</body>
</html>
```